A website for Medical Services to treat incontinence with a non-invasive product

We need to build a website to generate and convert new clients to schedule either treatment or book consultation (The device's name is QRV Floravia). Here are the reference sites for information only: (Please do not use the same style as this is the style we desperately want to change)
http://www.thepelvancenter.com/floravia-for-incontinence/
https://verdanomaktc.com/2018/04/13/urinary-incontinence/
https://verdanomaktc.com/non-invasive-lasers/female-incontinence/
http://www.drvorkin.com/services/wellness-services/sexual-health/qrv-floravia-urinary-incontinence-houston/

This is the vendor site:
https://corawellnex.com/

Target Market(s)

The targeted audience is mostly women between 30 - 75, suffering from stress incontinence due to childbirth and many other age-related conditions.

Industry/Entity Type

Health And Wellness

Number of Pages Required

4 page

Font styles to use
Sans Serif

Colors

Designer to choose colors to be used in the design.

Requirements
Must have
• How it works, How is it different from traditional invasive measures, What other people say about the treatment, video testimonials, FAQs, contact us, Book Appointment, latest promotions. maps, social media links
Nice to have
• The experienced urologist profile, office surroundings/interior, Reviews, number strips

```html
<!DOCTYPE html>
<html lang="en">
<head>
<meta charset="utf-8">
<title>Medical Treatment – Say No To Incontinence</title>
<link href="https://fonts.googleapis.com/css2?family=Cardo:wght@400;700&family=PT+Sans:wght@400;700&display=swap" rel="stylesheet">
<style>
:root{
  --cyan:#1ee3f7;
  --ink:#1d1d1d;
  --dark:#2a2a2a;
  --nav:#3a3a3a;
  --text:#333;
  --muted:#666;
  --light:#f7f7f7;
  --white:#fff;
  --line:#cfcfcf;
}
*{box-sizing:border-box;margin:0;padding:0}
html,body{width:1200px;height:3607px;overflow:hidden}
body{position:relative;background:var(--white);font-family:"PT Sans",Arial,sans-serif;color:var(--text);font-size:13px;line-height:1.6}
.abs{position:absolute}
.serif{font-family:"Cardo",Georgia,serif}
.btn{position:absolute;display:flex;align-items:center;justify-content:center;font-weight:700;font-size:12px;text-transform:uppercase;letter-spacing:.3px}
.btn-cyan{background:var(--cyan);color:var(--ink);box-shadow:4px 4px 0 -1px #bbb}
.btn-white{background:var(--white);color:var(--ink)}
.btn-ghost{border:2px solid var(--white);color:var(--white);background:rgba(0,0,0,.25)}

/* header */
.logo{left:161px;top:14px;font-family:"Cardo",Georgia,serif;font-weight:700;font-size:26px;color:var(--ink);letter-spacing:.2px}
.contact-chip{top:10px;display:flex;gap:10px;align-items:flex-start;font-size:11px;line-height:1.35}
.contact-chip .ic{width:30px;height:30px;background:var(--dark);display:flex;align-items:center;justify-content:center}
.contact-chip b{display:block;font-size:12px;color:var(--ink)}
.contact-chip span{color:var(--muted)}
.social-top{left:888px;top:12px;display:flex;gap:10px}
.social-top i{width:32px;height:32px;border-radius:50%;background:var(--ink);display:block}

/* hero */
.hero{left:0;top:0;width:1200px;height:660px}
.nav{left:161px;top:62px;width:878px;height:44px;background:var(--nav);display:flex;align-items:center;z-index:2}
.nav a{color:var(--white);font-size:11px;font-weight:700;text-transform:uppercase;text-decoration:none;padding:0 14px}
.nav .home{width:48px;height:44px;display:flex;align-items:center;justify-content:center}
.nav .quote{position:absolute;right:0;top:0;height:44px;width:156px;background:var(--cyan);color:var(--ink);display:flex;align-items:center;justify-content:center}
.hero-title{left:0;top:245px;width:1200px;text-align:center;font-family:"Cardo",Georgia,serif;font-weight:700;font-size:74px;color:var(--white);line-height:1.1}
.hero-copy{left:330px;top:350px;width:600px;text-align:center;color:var(--white);font-size:13px;line-height:1.7}
.scroll-line{left:217px;top:517px;width:2px;height:120px;background:var(--white)}
.scroll-dot{left:209px;top:612px;width:18px;height:30px;border:2px solid var(--white);border-radius:9px;background:rgba(0,0,0,.3)}

/* how it works */
.vline{width:2px;background:#555}
.section-title{font-family:"Cardo",Georgia,serif;font-weight:700;color:var(--ink);text-transform:uppercase}
.how-title{right:161px;top:692px;font-size:24px}
.how-copy{left:630px;top:740px;width:409px;text-align:right;font-size:12.5px;line-height:1.75}
.ph{position:absolute}
.diff-title{left:161px;top:1190px;width:520px;font-size:25px;line-height:1.35;letter-spacing:.3px}
.diff-copy{left:161px;top:1272px;width:512px;font-size:12px;line-height:1.75}

/* benefits */
.benefits{left:0;top:1481px;width:1200px;height:600px}
.ben-title{left:161px;top:1565px;font-family:"Cardo",Georgia,serif;font-size:26px;color:var(--cyan);text-transform:uppercase}
.ben-copy{left:161px;top:1622px;width:400px;color:var(--white);font-size:12.5px;line-height:1.8}
.card{position:absolute;width:159px;height:159px;border:2px solid var(--cyan);background:rgba(0,0,0,.45);color:var(--white);text-align:center;padding-top:16px}
.card h4{font-size:13px;text-transform:uppercase;margin-top:6px}
.card p{font-size:12px;line-height:1.4;padding:2px 18px 0}
.card u{display:block;font-size:12px;font-weight:700;margin-top:6px}
.card .plus{position:absolute;right:-2px;bottom:-2px;width:22px;height:22px;background:var(--cyan);color:var(--ink);font-weight:700;line-height:22px;font-size:16px}

/* appointment */
.light-band{left:24px;top:1972px;width:1152px;height:500px;background:var(--light)}
.appt{left:161px;top:2157px;width:878px;height:219px;background:var(--white);box-shadow:0 3px 14px rgba(0,0,0,.16)}
.appt h3{position:absolute;left:0;top:40px;width:100%;text-align:center;font-size:24px}
.field{position:absolute;top:98px;font-size:12px;color:var(--ink);border-bottom:1px solid var(--line);height:22px}

/* testimonials */
.testi-title{left:0;top:2430px;width:1200px;text-align:center;font-size:26px}
.video{position:absolute;top:2494px;width:416px;height:228px;box-shadow:0 3px 10px rgba(0,0,0,.2)}
.play{position:absolute;left:186px;top:92px;width:44px;height:44px;border-radius:50%;background:#f05a5a}
.play:after{content:"";position:absolute;left:17px;top:13px;border-left:14px solid #fff;border-top:9px solid transparent;border-bottom:9px solid transparent}
.t-name{position:absolute;top:2730px;width:416px;text-align:center;font-weight:700;font-size:14px;color:var(--ink);text-transform:uppercase}
.t-date{position:absolute;top:2752px;width:416px;text-align:center;font-size:11px;color:var(--ink)}
.arrow{position:absolute;top:2594px;width:26px;height:26px;border-radius:50%;background:var(--ink)}

/* faq */
.faq-title{left:0;top:2858px;width:1200px;text-align:center;font-size:26px}
.faq-copy{left:285px;top:2905px;width:630px;text-align:center;font-size:12.5px;line-height:1.75}
.faq{position:absolute;top:2975px;width:240px;text-align:center}
.faq h5{font-size:13px;text-transform:uppercase;color:var(--ink);line-height:1.35}
.faq i{display:block;width:20px;height:2px;background:var(--ink);margin:6px auto 8px}
.faq p{font-size:12px;line-height:1.6;color:var(--text)}
.dots{left:585px;top:3090px;display:flex;gap:5px}
.dots span{width:6px;height:6px;border-radius:50%;background:#333}
.dots span.on{background:var(--cyan)}

/* footer */
.foot-h{color:var(--white);font-weight:700;font-size:15px}
.foot-txt{color:#c9c9c9;font-size:11.5px;line-height:1.5}
.foot-row{position:absolute;left:161px;display:flex;gap:14px;align-items:flex-start;width:300px}
.foot-row svg{flex:none;margin-top:2px}
.f-social{left:820px;top:3430px;display:flex;gap:14px}
.f-social i{display:block;width:32px;height:32px;border-radius:50%;border:1px solid #888}
.copy-line{left:161px;top:3557px;width:878px;height:1px;background:#555}
.copyright{left:161px;top:3572px;font-size:11px;color:#bbb}
.policy{right:161px;top:3572px;font-size:11px;color:#bbb}
</style>
</head>
<body>

<!-- hero background with slanted base -->
<svg class="abs hero" width="1200" height="660" role="img" aria-label="Photo of a doctor and a female patient in a clinic, dimmed">
  <defs>
    <linearGradient id="heroGrad" x1="0" y1="0" x2="1" y2="1">
      <stop offset="0" stop-color="#4a4d52"/>
      <stop offset=".5" stop-color="#6a6c70"/>
      <stop offset="1" stop-color="#8a8a8c"/>
    </linearGradient>
  </defs>
  <polygon points="0,0 1200,0 1200,578 0,660" fill="url(#heroGrad)"/>
</svg>

<!-- header -->
<div class="abs" style="left:0;top:0;width:1200px;height:62px;background:var(--white)"></div>
<div class="abs logo">MEDICAL TREATMENT</div>
<div class="abs contact-chip" style="left:488px">
  <div class="ic"><svg width="16" height="16" viewBox="0 0 24 24"><path fill="#fff" d="M6.6 10.8a15.1 15.1 0 0 0 6.6 6.6l2.2-2.2c.3-.3.7-.4 1-.2 1.1.4 2.3.6 3.6.6.6 0 1 .4 1 1V20c0 .6-.4 1-1 1A17 17 0 0 1 3 4c0-.6.4-1 1-1h3.5c.6 0 1 .4 1 1 0 1.3.2 2.5.6 3.6.1.3 0 .7-.2 1z"/></svg></div>
  <div><b>CALL :</b><span>+1234567891</span></div>
</div>
<div class="abs contact-chip" style="left:613px">
  <div class="ic"><svg width="16" height="16" viewBox="0 0 24 24"><path fill="none" stroke="#fff" stroke-width="2" d="M3 6h18v12H3z M3 6l9 7 9-7"/></svg></div>
  <div><b>E-MAIL :</b><span>info@medicalcare-clinic.com</span></div>
</div>
<div class="abs social-top"><i></i><i></i><i></i><i></i></div>

<nav class="abs nav">
  <a class="home" href="#"><svg width="16" height="14" viewBox="0 0 16 14"><path fill="#fff" d="M8 0l8 7h-2v7H10V9H6v5H2V7H0z"/></svg></a>
  <a href="#">Home</a><a href="#">About</a><a href="#">How it works</a><a href="#">How it is different</a><a href="#">Testimonials</a><a href="#">FAQs</a><a href="#">Contact us</a>
  <a class="quote" href="#">Request a quote</a>
</nav>

<h1 class="abs hero-title">Say No To Incontinence</h1>
<p class="abs hero-copy">Lorem Ipsum is simply dummy text of the printing and typesetting industry. Lorem Ipsum has been the industry's standard dummy text ever since the 1500s, when an unknown printer took a galley of type</p>
<a class="btn btn-white" style="left:464px;top:428px;width:128px;height:43px">Learn more</a>
<a class="btn btn-ghost" style="left:608px;top:428px;width:125px;height:43px;text-transform:none;font-size:13px">Contact Us</a>
<div class="abs scroll-line"></div>
<div class="abs scroll-dot"></div>

<!-- how it works -->
<div class="abs vline" style="left:218px;top:685px;height:170px"></div>
<h2 class="abs section-title how-title">How it works</h2>
<p class="abs how-copy">Lorem Ipsum is simply dummy text of the printing and typesetting industry Lorem Ipsum has been the industry's standard dummy text ever since the 1500s, when an unknown printer took a galley of type and scrambled it to make a type specimen book. It has survived not only five centuries, but also the leap into electronic typesetting, remaining essentially unchanged. It was popularised in the 1960s with the release of Letraset sheets containing Lorem Ipsum passages,and more recently with desktop publishing software like Aldus</p>
<a class="btn btn-cyan" style="left:928px;top:918px;width:106px;height:44px">Learn more</a>

<div class="ph" role="img" aria-label="Photo of a smiling woman seated on a white sofa" style="left:161px;top:875px;width:368px;height:217px;background:linear-gradient(135deg,#5c5f63,#8b8d90 60%,#6e7074)"></div>
<div class="ph" role="img" aria-label="Photo of the QRV Floravia treatment chair with its control console" style="left:688px;top:1005px;width:423px;height:397px;background:radial-gradient(ellipse at 50% 50%,#e4eef3 0%,#f6f9fb 60%,#fff 100%)"></div>

<h2 class="abs section-title diff-title">How is it different from traditional invasive measures</h2>
<p class="abs diff-copy">Lorem Ipsum is simply dummy text of the printing and typesetting industry Lorem Ipsum has been the industry's standard dummy text ever since the 1500s, when an unknown printer took a galley of type and scrambled it to make a type specimen book. It has survived not only five centuries, but also the leap into electronic typesetting, remaining essentially unchanged.</p>
<a class="btn btn-cyan" style="left:163px;top:1378px;width:104px;height:46px">Learn more</a>

<!-- light band under benefits -->
<div class="abs light-band"></div>

<!-- benefits -->
<svg class="abs benefits" width="1200" height="600" role="img" aria-label="Dimmed photo of doctors consulting with a patient">
  <defs>
    <linearGradient id="benGrad" x1="0" y1="0" x2="1" y2="0">
      <stop offset="0" stop-color="#3c3e42"/>
      <stop offset=".5" stop-color="#55575b"/>
      <stop offset="1" stop-color="#45474b"/>
    </linearGradient>
  </defs>
  <polygon points="0,0 1200,0 1200,491 600,582 0,491" fill="url(#benGrad)"/>
</svg>
<h2 class="abs ben-title">Benefits of QRV Floravia</h2>
<p class="abs ben-copy">Lorem Ipsum is simply dummy text of the printing and typesetting industry. Lorem Ipsum has been the industry's standard dummy text ever since the 1500s,<br>when an unknown printer took a galley of type and scrambled it to make a type specimen book. It has survived not only five centuries, but also the leap into electronic typesetting...</p>
<a class="btn btn-white" style="left:164px;top:1799px;width:127px;height:43px">View more</a>

<div class="card" style="left:671px;top:1570px">
  <svg width="28" height="24" viewBox="0 0 28 24"><path d="M2 13l8 8L26 3" fill="none" stroke="#fff" stroke-width="4"/></svg>
  <h4>Drug free</h4><p>Lorem Ipsum is dummy text Printing text</p><u>Learn More</u><span class="plus">+</span>
</div>
<div class="card" style="left:878px;top:1570px">
  <svg width="28" height="24" viewBox="0 0 28 24"><path d="M2 13l8 8L26 3" fill="none" stroke="#fff" stroke-width="4"/></svg>
  <h4>Surgery free</h4><p>Lorem Ipsum is dummy text Printing text</p><u>Learn More</u><span class="plus">+</span>
</div>
<div class="card" style="left:671px;top:1758px">
  <svg width="28" height="24" viewBox="0 0 28 24"><path d="M2 13l8 8L26 3" fill="none" stroke="#fff" stroke-width="4"/></svg>
  <h4>Totally non-invasive</h4><p>Lorem Ipsum is dummy text Printing text</p><u>Learn More</u><span class="plus">+</span>
</div>
<div class="card" style="left:878px;top:1758px">
  <svg width="28" height="24" viewBox="0 0 28 24"><path d="M2 13l8 8L26 3" fill="none" stroke="#fff" stroke-width="4"/></svg>
  <h4>Long lasting</h4><p>Lorem Ipsum is dummy text Printing text</p><u>Learn More</u><span class="plus">+</span>
</div>

<!-- appointment -->
<div class="abs vline" style="left:599px;top:2063px;height:94px;background:#777"></div>
<section class="abs appt">
  <h3 class="section-title">Book an appointment</h3>
  <div class="field" style="left:32px;width:100px">First Name</div>
  <div class="field" style="left:176px;width:150px">E-mail</div>
  <div class="field" style="left:377px;width:130px">Phone</div>
  <div class="field" style="left:520px;width:326px">Message :</div>
  <a class="btn" style="left:375px;top:144px;width:125px;height:44px;background:var(--cyan);color:var(--ink);font-size:13px">Submit</a>
</section>

<!-- testimonials -->
<h2 class="abs section-title testi-title">Testimonials</h2>
<div class="arrow" style="left:105px"><svg width="26" height="26" viewBox="0 0 26 26"><path d="M15 8l-5 5 5 5" fill="none" stroke="#fff" stroke-width="2.5"/></svg></div>
<div class="arrow" style="left:1067px"><svg width="26" height="26" viewBox="0 0 26 26"><path d="M11 8l5 5-5 5" fill="none" stroke="#fff" stroke-width="2.5"/></svg></div>
<div class="video" role="img" aria-label="Video testimonial still of a patient with her doctor" style="left:161px;background:linear-gradient(120deg,#c7a58c,#e9e5e2 55%,#d9dde2)"><span class="play"></span></div>
<div class="video" role="img" aria-label="Video testimonial still of a clinic examination room" style="left:623px;background:linear-gradient(120deg,#b7d3df,#e6eef2 55%,#8fb6c8)"><span class="play"></span></div>
<div class="t-name" style="left:161px">Marina Holt</div>
<div class="t-date" style="left:161px">( 05 june - 2018 )</div>
<div class="t-name" style="left:623px">Marina Holt</div>
<div class="t-date" style="left:623px">( 05 june - 2018 )</div>

<div class="abs" style="left:0;top:2818px;width:1200px;height:1px;background:#ddd"></div>

<!-- faq -->
<h2 class="abs section-title faq-title">Frequently asked questions</h2>
<p class="abs faq-copy">Lorem Ipsum is simply dummy text of the printing and typesetting industry.Lorem Ipsum has been the industry's standard dummy text ever since the 1500s, when an unknown printer took a galley of type and scrambled it to make a type</p>
<div class="faq" style="left:147px"><h5>Who does Floravia<br>work for?</h5><i></i><p>The treatment is indicated for women with stress incontinence incontinence</p></div>
<div class="faq" style="left:480px"><h5>How does the treat-<br>ment work?</h5><i></i><p>Floravia is a non-surgical, non-invasive treatment for stress or urge urinary ...</p></div>
<div class="faq" style="left:811px"><h5>Is Floravia covered<br>by insurance?</h5><i></i><p>The treatment is FDA approved. We believe Floravia is an investment in you.</p></div>
<div class="abs dots"><span></span><span></span><span class="on"></span></div>

<!-- footer -->
<svg class="abs" style="left:0;top:3140px" width="1200" height="467">
  <polygon points="0,95 909,10 1200,88 1200,467 0,467" fill="#2b2b2b"/>
  <line x1="909" y1="10" x2="909" y2="200" stroke="#777" stroke-width="1.5"/>
</svg>
<div class="abs foot-h" style="left:161px;top:3364px">Contact Information</div>
<div class="foot-row" style="top:3424px"><svg width="16" height="16" viewBox="0 0 24 24"><path fill="#fff" d="M6.6 10.8a15.1 15.1 0 0 0 6.6 6.6l2.2-2.2c.3-.3.7-.4 1-.2 1.1.4 2.3.6 3.6.6.6 0 1 .4 1 1V20c0 .6-.4 1-1 1A17 17 0 0 1 3 4c0-.6.4-1 1-1h3.5c.6 0 1 .4 1 1 0 1.3.2 2.5.6 3.6.1.3 0 .7-.2 1z"/></svg><span class="foot-txt">Phone : +1234567891</span></div>
<div class="foot-row" style="top:3454px"><svg width="16" height="18" viewBox="0 0 16 20"><path fill="#fff" d="M8 0a7 7 0 0 0-7 7c0 5 7 13 7 13s7-8 7-13a7 7 0 0 0-7-7zm0 10a3 3 0 1 1 0-6 3 3 0 0 1 0 6z"/></svg><span class="foot-txt">Lorem Ipsum is dummy text industry<br>printing and dummy text...</span></div>
<div class="foot-row" style="top:3502px"><svg width="16" height="14" viewBox="0 0 24 20"><path fill="none" stroke="#fff" stroke-width="2" d="M2 2h20v16H2z M2 2l10 8 10-8"/></svg><span class="foot-txt">info@medicalcare-clinic.com</span></div>

<div class="abs foot-h" style="left:491px;top:3364px">Quick Link</div>
<div class="abs foot-txt" style="left:491px;top:3422px;line-height:1.85">Home<br>About<br>How It Works<br>How It Is Different</div>
<div class="abs foot-txt" style="left:654px;top:3422px;line-height:1.85">Testimonials<br>FAQs<br>Contact Us</div>

<div class="abs" style="left:837px;top:3360px;color:#fff;font-size:21px">Stay Connected</div>
<div class="abs f-social"><i></i><i></i><i></i><i></i></div>

<div class="abs copy-line"></div>
<div class="abs copyright">Copyright © 2018 Medical Treatment. All rights reserved.</div>
<div class="abs policy">Privacy Policy &nbsp;|&nbsp; Terms and Condition</div>

</body>
</html>
```